riverstonelightcare - healing business promotion

I have and energy / intuitive healing and kinesiology business. working with people who are looking for healing outside of the modern medical model, who have tried but failed in their search for understanding their conditions and why health and or happiness eludes them. the healing is done with love, patience and understanding. I am looking to be taken seriously with my presentation and to reach a person who may be deterred by the thought of angels and intuition! but to not exclude those that are attracted to that also.

Industry/Entity Type

Medical

Contact Information for Business Card

riverstonelightcare
calm clear gentle energy renewal method
tamsin corrine hale
energy healing / kinesiology and neurotraining
0417362815 07 4186 2751
home visits available for Harlow Bay and Ridgelands
t.chale@maildrop-example.net

Requirements
Should not have
• Primary colours

```html
<!DOCTYPE html>
<html lang="en">
<head>
<meta charset="utf-8">
<title>Riverstone Light Care – Business Card</title>
<link rel="stylesheet" href="https://fonts.googleapis.com/css2?family=Gelasio:wght@400;500&display=swap">
<style>
  :root {
    --page-bg: #e4e5e7;
    --card-top-light: #ffffff;
    --card-top-shade: #d9d9da;
    --divider-dark: #6e6f72;
    --divider-light: #b9babc;
    --sage: #6fae8c;
    --mint-blue: #a9cfd6;
    --blush: #f1a9c8;
    --ink: #1c1c1c;
    --ink-soft: #3a3a3a;
    --tagline: #8a8a8a;
  }
  * { margin: 0; padding: 0; box-sizing: border-box; }
  html, body { width: 1200px; height: 861px; overflow: hidden; }
  body {
    background: var(--page-bg);
    display: flex;
    align-items: center;
    justify-content: center;
    font-family: "Gelasio", Georgia, serif;
  }
  .business-card {
    width: 880px;
    height: 530px;
    border-radius: 26px;
    overflow: hidden;
    display: flex;
    flex-direction: column;
    box-shadow: 0 18px 40px rgba(0,0,0,0.18);
  }
  .card-brand {
    height: 262px;
    background: linear-gradient(180deg, var(--card-top-light) 0%, #f3f3f3 55%, var(--card-top-shade) 100%);
    display: flex;
    flex-direction: column;
    align-items: center;
    justify-content: flex-end;
    padding-bottom: 22px;
  }
  .brand-name {
    font-size: 38px;
    font-weight: 400;
    color: var(--ink);
    letter-spacing: 0.5px;
  }
  .brand-tagline {
    margin-top: 8px;
    font-size: 14px;
    letter-spacing: 3px;
    color: var(--tagline);
  }
  .card-divider {
    height: 12px;
    background: linear-gradient(180deg, var(--divider-light) 0 3px, var(--divider-dark) 3px 6px, var(--divider-light) 6px 9px, #8f9093 9px 12px);
  }
  .card-contact {
    flex: 1;
    background: linear-gradient(100deg, var(--sage) 0%, #8fc0ae 28%, var(--mint-blue) 52%, #e4b6cb 78%, var(--blush) 100%);
    text-align: center;
    padding-top: 24px;
    color: var(--ink);
  }
  .person-name {
    font-size: 36px;
    font-weight: 400;
    line-height: 1.1;
  }
  .person-role {
    font-size: 16px;
    font-weight: 500;
    margin-top: 4px;
  }
  .contact-list {
    list-style: none;
    margin-top: 20px;
    font-size: 18px;
    line-height: 1.45;
    color: var(--ink-soft);
  }
</style>
</head>
<body>
  <main class="business-card">
    <section class="card-brand">
      <h1 class="brand-name">Riverstone Light Care</h1>
      <p class="brand-tagline">calm clear gentle energy renewal method</p>
    </section>
    <div class="card-divider"></div>
    <section class="card-contact">
      <h2 class="person-name">Tamsin Corrine Hale</h2>
      <p class="person-role">Energy Healing / Kinesiology and Neurotraining</p>
      <ul class="contact-list">
        <li>Phone:&nbsp; 0417362815</li>
        <li>Mobile: 07 4186 2751</li>
        <li>E-mail: t.chale@maildrop-example.net</li>
        <li>Home visits available for Harlow Bay and Ridgelands</li>
      </ul>
    </section>
  </main>
</body>
</html>
```